Business Card Design

Selling Televisions, Velorin, Kavo, Drelvatek, Morenzi
The latest models, sizes ranging from 22"- 75"
Surround Sounds, Sound Bars and Wall Mounts

Target Market(s)

Mainly males/boys/blokes etc

Industry/Entity Type

Business

Contact Information for Business Card

Glen Rudd
07812459306
glrudd@quillnetmail.com

Requirements
Must have
• simplistic design, probably just 2 of the images used

clarity essential
Nice to have
• Metallic if possible

```html
<!DOCTYPE html>
<html lang="en">
<head>
<meta charset="utf-8">
<title>Glen Rudd – Business Card</title>
<link rel="stylesheet" href="https://fonts.googleapis.com/css2?family=Michroma&family=Oswald:wght@400&display=swap">
<style>
  :root {
    --page-bg: #3b3937;
    --card-base: #1c1c1c;
    --card-light: #3a3a3a;
    --card-streak: rgba(255,255,255,0.035);
    --bar-bg: #050505;
    --text-light: #f2f2f2;
    --text-soft: #d9d9d9;
    --metal-top: #ffffff;
    --metal-mid: #b9b9b9;
    --metal-low: #e6e6e6;
    --photo-a: #6a6f80;
    --photo-b: #2b2f45;
    --photo-c: #151515;
  }
  * { box-sizing: border-box; margin: 0; padding: 0; }
  html, body {
    width: 1200px; height: 840px; overflow: hidden;
    background: var(--page-bg);
  }
  .card {
    position: absolute; left: 100px; top: 80px;
    width: 1000px; height: 680px;
    background:
      repeating-linear-gradient(90deg, var(--card-streak) 0 1px, transparent 1px 4px),
      radial-gradient(ellipse at 50% 30%, var(--card-light) 0%, var(--card-base) 70%);
    box-shadow: 0 10px 30px rgba(0,0,0,0.5);
    overflow: hidden;
  }
  .card-name {
    position: absolute; top: 162px; left: 0; width: 100%;
    text-align: center;
    font-family: "Michroma", sans-serif;
    font-size: 70px; letter-spacing: 4px;
    text-transform: uppercase;
    background: linear-gradient(180deg, var(--metal-top) 0%, var(--metal-mid) 55%, var(--metal-low) 100%);
    -webkit-background-clip: text; background-clip: text;
    color: transparent;
  }
  .card-contact {
    position: absolute; top: 252px; left: 0; width: 100%;
    display: flex; justify-content: center; align-items: center; gap: 26px;
    font-family: "Oswald", sans-serif; font-size: 31px;
    color: var(--text-light);
  }
  .contact-item { display: flex; align-items: center; gap: 8px; }
  .contact-icon { width: 28px; height: 28px; fill: var(--text-light); }
  .product-photo {
    position: absolute; left: 75px; top: 312px;
    width: 341px; height: 284px;
    background: linear-gradient(160deg, var(--photo-a) 0%, var(--photo-b) 55%, var(--photo-c) 100%);
    border-radius: 4px;
  }
  .feature-bar {
    position: absolute; right: 0; height: 57px;
    background: var(--bar-bg);
    display: flex; justify-content: flex-end; align-items: center;
    padding-right: 40px; gap: 12px;
    font-family: "Oswald", sans-serif; font-size: 23px;
    color: var(--text-light);
  }
  .feature-bar--brands { left: 402px; top: 334px; }
  .feature-bar--audio { left: 440px; top: 402px; }
  .feature-bar--sizes { left: 477px; top: 471px; }
  .move-icon { width: 20px; height: 20px; fill: var(--text-soft); }
</style>
</head>
<body>
  <main class="card">
    <h1 class="card-name">Glen Rudd</h1>

    <div class="card-contact">
      <span class="contact-item">
        <svg class="contact-icon" viewBox="0 0 24 24" aria-hidden="true">
          <path d="M7 2h10a1.5 1.5 0 0 1 1.5 1.5v17A1.5 1.5 0 0 1 17 22H7a1.5 1.5 0 0 1-1.5-1.5v-17A1.5 1.5 0 0 1 7 2zm0.5 3v13h9V5zm4.5 14.2a1 1 0 1 0 0 2 1 1 0 0 0 0-2z"/>
        </svg>
        07812459306
      </span>
      <span class="contact-item">
        <svg class="contact-icon" viewBox="0 0 24 24" aria-hidden="true">
          <path d="M2 5h20v14H2zm2 1.5 8 6.5 8-6.5z"/>
        </svg>
        glrudd@quillnetmail.com
      </span>
    </div>

    <div class="product-photo" role="img" aria-label="Photograph of two large flat-screen televisions showing landscape and city night scenes"></div>

    <p class="feature-bar feature-bar--brands">
      Selling Televisions, Velorin, Kavo, Drelvatek, Morenzi
      <svg class="move-icon" viewBox="0 0 20 20" aria-hidden="true"><path d="M10 0l3 4h-2v5h5V7l4 3-4 3v-2h-5v5h2l-3 4-3-4h2v-5H4v2l-4-3 4-3v2h5V4H7z"/></svg>
    </p>
    <p class="feature-bar feature-bar--audio">
      Surround Sounds, Sound Bars and Wall Mounts
      <svg class="move-icon" viewBox="0 0 20 20" aria-hidden="true"><path d="M10 0l3 4h-2v5h5V7l4 3-4 3v-2h-5v5h2l-3 4-3-4h2v-5H4v2l-4-3 4-3v2h5V4H7z"/></svg>
    </p>
    <p class="feature-bar feature-bar--sizes">
      The latest models, sizes ranging from 22"- 75"
      <svg class="move-icon" viewBox="0 0 20 20" aria-hidden="true"><path d="M10 0l3 4h-2v5h5V7l4 3-4 3v-2h-5v5h2l-3 4-3-4h2v-5H4v2l-4-3 4-3v2h5V4H7z"/></svg>
    </p>
  </main>
</body>
</html>
```